Australian Craft Distillery needs poster layout for its awesome Manifesto

Tall Finch's a small craft distillery based in the Brook Flats of Western Australia producing award-winning vodkas and gin. Check out our website www.tallfinchs-example.com.au to get a feel for our design aesthetic, especially from our bottle design. We are "Small Batch Liquors - Out of the Brook Flats". Everything we do reflects that.
We have a manifesto - The Tall Finch's Manifesto -that we proudly display in our tasting room, and was used as a basis for an artwork in our entry.
We've had a number of customers ask to buy a poster of the manifesto (attached) so I want to commission a more professional design than the current layout which was put together in Word! (yes I know, I'm sorry, I did move it into Illustrator later).
I think the text flows in a sequential order so I'm looking for a design that you read from start to finish rather than a random collection of statements. I'd like to include our logo in the design somewhere but it doesn't have to be front and centre. There is a secondary logo device as well - the interlocked T and F on the label which could be used. I'm assuming the print will be simple black on either a plain background or a "craft background" similar to the labels. Our current fonts are SchmutzICG for text and VeneerTwo for headings. The label uses Haymaker and Gin-Rough.
Print size will be A3 (prefer the design to be to this proportion and portrait orientation) and bigger up to A1. We'll print the final design on the back of t-shirts for staff as well. If I was going to sum up our style in a couple of words it would be "intelligently irreverent" Have fun with this, I certainly did writing it!

```html
<!DOCTYPE html>
<html lang="en">
<head>
<meta charset="utf-8">
<title>The Tall Finch's Manifesto – Poster</title>
<link rel="stylesheet" href="https://fonts.googleapis.com/css2?family=Oswald:wght@400;700&family=Special+Elite&display=swap">
<style>
  :root {
    --backdrop: #141414;
    --paper-light: #d6b46c;
    --paper: #c8a35a;
    --paper-dark: #b48c45;
    --ink: #2b2313;
    --ink-soft: rgba(60, 40, 10, .45);
  }
  * { margin: 0; padding: 0; box-sizing: border-box; }
  html, body {
    width: 1200px; height: 1200px; overflow: hidden;
    background: var(--backdrop);
  }
  .poster {
    position: absolute; left: 225px; top: 70px;
    width: 753px; height: 1056px;
    background:
      radial-gradient(ellipse at 30% 15%, var(--paper-light) 0%, transparent 60%),
      radial-gradient(ellipse at 80% 85%, var(--paper-dark) 0%, transparent 65%),
      var(--paper);
    color: var(--ink);
    overflow: hidden;
  }
  .masthead {
    position: absolute; top: 42px; left: 0; width: 100%;
    text-align: center; font-family: 'Oswald', sans-serif;
  }
  .masthead__the { font-weight: 400; font-size: 15px; letter-spacing: 8px; line-height: 22px; }
  .masthead__name { font-weight: 700; font-size: 42px; line-height: 50px; letter-spacing: 1px; }
  .masthead__sub { font-weight: 400; font-size: 14px; letter-spacing: 8px; line-height: 22px; }
  .bottle {
    position: absolute; left: 278px; top: 194px;
    width: 199px; height: 768px; overflow: visible;
  }
  .bottle-shadow {
    position: absolute; left: 258px; top: 956px; width: 240px; height: 18px;
    border-radius: 50%;
    background: radial-gradient(ellipse, var(--ink-soft) 0%, transparent 70%);
  }
  .bottle text { fill: var(--ink); }
  .bottle .on-ink { fill: var(--paper-light); }
  .cond { font-family: 'Oswald', sans-serif; font-weight: 700; }
  .type { font-family: 'Special Elite', monospace; }
  .ink-band { fill: var(--ink); }
</style>
</head>
<body>
<main class="poster">
  <header class="masthead">
    <div class="masthead__the">THE</div>
    <div class="masthead__name">TALL FINCH'S</div>
    <div class="masthead__sub">MAINFESTO</div>
  </header>

  <div class="bottle-shadow"></div>

  <svg class="bottle" viewBox="0 0 199 768" aria-label="The Tall Finch's Manifesto set as a column of type in the outline of a bottle">
    <g class="bottle__neck">
      <text class="cond" x="52" y="13" font-size="14" textLength="95" lengthAdjust="spacingAndGlyphs">RISE EARLY</text>
      <text class="type" x="52" y="25" font-size="8" textLength="95" lengthAdjust="spacingAndGlyphs">rest when you must</text>
      <text class="cond" x="52" y="39" font-size="12" textLength="95" lengthAdjust="spacingAndGlyphs">BREW SOMETHING</text>
      <text class="type" x="52" y="50" font-size="7" textLength="95" lengthAdjust="spacingAndGlyphs">share the first pour</text>
      <text class="type" x="52" y="66" font-size="16" textLength="95" lengthAdjust="spacingAndGlyphs">TASTE</text>
      <text class="type" x="52" y="77" font-size="7" textLength="95" lengthAdjust="spacingAndGlyphs">then taste again</text>
      <text class="cond" x="52" y="91" font-size="12" textLength="95" lengthAdjust="spacingAndGlyphs">STAY CURIOUS</text>
      <text class="type" x="52" y="101" font-size="6.5" textLength="95" lengthAdjust="spacingAndGlyphs">ask one more question</text>
      <text class="cond" x="52" y="116" font-size="10" textLength="108" lengthAdjust="spacingAndGlyphs">RAISE A GLASS TO FRIENDS</text>
    </g>

    <g class="bottle__body">
      <text class="cond" x="0" y="146" font-size="24" textLength="199" lengthAdjust="spacingAndGlyphs">KEEP IT HONEST</text>
      <text class="type" x="0" y="163" font-size="13" textLength="199" lengthAdjust="spacingAndGlyphs">say what you mean</text>
      <text class="type" x="0" y="179" font-size="13" textLength="199" lengthAdjust="spacingAndGlyphs">mean what you say</text>
      <text class="cond" x="0" y="207" font-size="26" textLength="199" lengthAdjust="spacingAndGlyphs">BUILD THINGS</text>
      <text class="type" x="0" y="223" font-size="11" textLength="199" lengthAdjust="spacingAndGlyphs">with your own two hands</text>
      <text class="type" x="0" y="247" font-size="22" textLength="199" lengthAdjust="spacingAndGlyphs">SLOWLY</text>
      <text class="cond" x="0" y="267" font-size="16" textLength="199" lengthAdjust="spacingAndGlyphs">GOOD WORK TAKES TIME</text>
      <text class="type" x="0" y="286" font-size="14" textLength="199" lengthAdjust="spacingAndGlyphs">wander off the map</text>
      <text class="type" x="0" y="303" font-size="14" textLength="199" lengthAdjust="spacingAndGlyphs">FIND A NEW ROAD</text>

      <rect class="ink-band" x="0" y="312" width="199" height="28"/>
      <text class="cond on-ink" x="8" y="334" font-size="20" textLength="183" lengthAdjust="spacingAndGlyphs">POUR WITH CARE</text>

      <text class="cond" x="0" y="364" font-size="22" textLength="199" lengthAdjust="spacingAndGlyphs">MISTAKES HAPPEN</text>
      <text class="type" x="0" y="380" font-size="11" textLength="199" lengthAdjust="spacingAndGlyphs">own them, fix them,</text>
      <text class="type" x="0" y="394" font-size="11" textLength="199" lengthAdjust="spacingAndGlyphs">and carry on</text>
      <text class="type" x="0" y="419" font-size="22" textLength="199" lengthAdjust="spacingAndGlyphs">LAUGH MORE</text>
      <text class="type" x="0" y="436" font-size="12" textLength="199" lengthAdjust="spacingAndGlyphs">especially at yourself</text>
      <text class="cond" x="0" y="463" font-size="24" textLength="199" lengthAdjust="spacingAndGlyphs">LISTEN FIRST</text>
      <text class="type" x="0" y="479" font-size="11" textLength="199" lengthAdjust="spacingAndGlyphs">then speak kindly</text>
      <text class="type" x="0" y="504" font-size="22" textLength="199" lengthAdjust="spacingAndGlyphs">BE GENEROUS</text>
      <text class="cond" x="0" y="522" font-size="14" textLength="199" lengthAdjust="spacingAndGlyphs">WITH TIME AND PRAISE</text>
      <text class="cond" x="0" y="550" font-size="26" textLength="199" lengthAdjust="spacingAndGlyphs">SLOW DOWN</text>
      <text class="type" x="0" y="566" font-size="11" textLength="199" lengthAdjust="spacingAndGlyphs">the view is better</text>
      <text class="type" x="0" y="590" font-size="20" textLength="199" lengthAdjust="spacingAndGlyphs">LEARN DAILY</text>
      <text class="type" x="0" y="606" font-size="11" textLength="199" lengthAdjust="spacingAndGlyphs">teach what you know</text>
      <text class="cond" x="0" y="633" font-size="22" textLength="199" lengthAdjust="spacingAndGlyphs">CHANGE IS COMING</text>
      <text class="type" x="0" y="651" font-size="13" textLength="199" lengthAdjust="spacingAndGlyphs">lean into it</text>
      <text class="type" x="0" y="674" font-size="14" textLength="199" lengthAdjust="spacingAndGlyphs">CHOOSE YOUR PATH</text>
      <text class="type" x="0" y="694" font-size="12" textLength="199" lengthAdjust="spacingAndGlyphs">and enjoy the ride</text>

      <rect class="ink-band" x="0" y="712" width="199" height="56"/>
      <text class="cond on-ink" x="7" y="737" font-size="21" textLength="185" lengthAdjust="spacingAndGlyphs">MAKE IT YOUR OWN</text>
      <text class="cond on-ink" x="7" y="761" font-size="21" textLength="185" lengthAdjust="spacingAndGlyphs">AND MAKE IT GOOD</text>
    </g>
  </svg>
</main>
</body>
</html>
```